Q5 Pops (CBD candy infused with Delta-8)

The proposed logo are two pool table balls. One is a D and the other is an 8, its a brand and we need a label for Gummy human treats. This treats are being infused with Delt-8. I i will upload examples only. The example is of the type of labels needed (package and label for bottle)

Target Market(s)

Your professionals

Font styles to use
Sans Serif

Requirements
Must have
• Youthful look
Nice to have
• Consider using the Delta symbol instead of the D.
Also, I provided a sample of a label that's used on two type of packages.

```html
<!DOCTYPE html>
<html lang="en">
<head>
<meta charset="utf-8">
<title>Q5 Pops – CBD Candy Pouch Label</title>
<link rel="stylesheet" href="https://fonts.googleapis.com/css2?family=Barlow:wght@400;600;700&family=Barlow+Semi+Condensed:wght@700&display=swap">
<style>
  :root {
    --backdrop: #e6e6e6;
    --pouch-black: #1b1c1b;
    --pouch-green: #22802a;
    --pouch-green-mid: #1a5e1f;
    --pouch-green-deep: #0f3812;
    --accent-green: #3cf21c;
    --accent-blue: #3b8fd0;
    --text-white: #ffffff;
    --text-soft: #d9dcd9;
  }
  * { margin: 0; padding: 0; box-sizing: border-box; }
  html, body {
    width: 1200px; height: 787px; overflow: hidden;
    background: var(--backdrop);
    font-family: "Barlow", sans-serif;
  }
  .canvas { position: relative; width: 1200px; height: 787px; }

  .pouch {
    position: absolute; left: 423px; top: 118px;
    width: 354px; height: 584px;
    background: linear-gradient(180deg,
      var(--pouch-green) 0%, var(--pouch-green-mid) 40%,
      var(--pouch-green-deep) 68%, var(--pouch-black) 100%);
    border-radius: 4px;
    overflow: hidden;
  }
  .pouch__seal {
    position: absolute; left: 0; top: 0; width: 100%; height: 72px;
    background: var(--pouch-black);
  }
  .pouch__hang-hole {
    position: absolute; left: 120px; top: 30px;
    width: 114px; height: 18px; border-radius: 9px;
    background: var(--backdrop);
  }
  .dose-corner {
    position: absolute; left: 0; top: 72px;
    width: 80px; height: 88px;
  }
  .dose-corner__text {
    position: absolute; left: 28px; top: 4px; width: 52px;
    text-align: center; color: var(--accent-blue);
    font-family: "Barlow Semi Condensed", sans-serif; font-weight: 700;
    line-height: 0.95;
  }
  .dose-corner__value, .dose-corner__unit { font-size: 22px; display: block; }
  .dose-corner__each {
    font-size: 9px; display: block; letter-spacing: 1px;
    font-family: "Barlow", sans-serif; font-weight: 400; margin-top: 2px;
  }

  .brand-mark {
    position: absolute; left: 0; top: 118px; width: 100%; height: 150px;
    display: flex; align-items: center; justify-content: center; gap: 16px;
  }
  .brand-mark__dot {
    width: 120px; height: 120px; border-radius: 50%;
    background: var(--accent-blue);
    flex: none;
  }
  .brand-mark__name {
    color: var(--text-white); font-weight: 700; font-size: 40px;
    line-height: 1; white-space: nowrap;
  }

  .product-title {
    position: absolute; left: 0; top: 296px; width: 100%;
    text-align: center; color: var(--accent-green);
    font-weight: 700; font-size: 50px; letter-spacing: 1.5px;
    text-transform: uppercase; line-height: 1;
  }
  .product-subtitle {
    position: absolute; left: 0; top: 346px; width: 100%;
    text-align: center; color: var(--text-white);
    font-family: "Barlow Semi Condensed", sans-serif;
    font-weight: 700; font-size: 23px; line-height: 1.05;
    text-transform: uppercase; letter-spacing: 0.5px;
  }
  .pack-count {
    position: absolute; left: 0; top: 480px; width: 100%;
    text-align: center; color: var(--text-soft);
    font-size: 13px; letter-spacing: 2px; text-transform: uppercase;
  }
</style>
</head>
<body>
<main class="canvas">
  <section class="pouch" aria-label="Q5 Pops candy pouch">
    <div class="pouch__seal"><div class="pouch__hang-hole"></div></div>

    <div class="dose-corner">
      <svg width="80" height="88" viewBox="0 0 80 88" aria-hidden="true">
        <polygon points="0,0 78,0 0,86" fill="var(--pouch-black)"/>
      </svg>
      <p class="dose-corner__text">
        <span class="dose-corner__value">30</span>
        <span class="dose-corner__unit">MG</span>
        <span class="dose-corner__each">EACH</span>
      </p>
    </div>

    <div class="brand-mark">
      <span class="brand-mark__dot"></span>
      <span class="brand-mark__name">Q5 Pops</span>
    </div>

    <h1 class="product-title">Q5 Pops</h1>
    <p class="product-subtitle">CBD Candy Infused<br>with Delta-8</p>
    <p class="pack-count">30 per bag / 30mg each</p>
  </section>
</main>
</body>
</html>
```